Bright Lantern Studios Business Card Design

Doug Farley

Managing Partner

Doug@BrightLanternStudios.com

BrightLanternStudios.com

502-417-2356

Industry/Entity Type

Photographer

Contact Information for Business Card

Doug Farley

Managing Partner

Doug@BrightLanternStudios.com

BrightLanternStudios.com

502-417-2356

Requirements
Must have
• Must show that I am a pavlo trusted photographer

```html
<!DOCTYPE html>
<html lang="en">
<head>
<meta charset="utf-8">
<title>Bright Lantern Studios Business Card</title>
<link rel="stylesheet" href="https://fonts.googleapis.com/css2?family=Questrial&family=Montserrat:wght@700&family=Open+Sans:wght@400&display=swap">
<style>
  :root {
    --backdrop: #3a3a3a;
    --card: #1f1f21;
    --white: #ffffff;
    --silver: #c9c9c9;
    --band-dark: #5d5f5f;
    --band-light: #c4c4c4;
    --muted: #d6d6d6;
    --badge-green: #3f9a4a;
    --badge-gold: #f1b22b;
  }
  * { margin: 0; padding: 0; box-sizing: border-box; }
  html, body { width: 799px; height: 1200px; overflow: hidden; }
  body {
    background: var(--backdrop);
    position: relative;
    font-family: "Questrial", sans-serif;
  }
  .card {
    position: absolute;
    left: 80px;
    width: 640px;
    height: 366px;
    background: var(--card);
    overflow: hidden;
  }
  .card-front { top: 160px; }
  .card-back { top: 680px; }

  /* Front */
  .front-mark {
    position: absolute;
    left: 0; right: 0; top: 118px;
    display: flex; flex-direction: column; align-items: center; gap: 22px;
  }
  .mark-dot {
    width: 70px; height: 70px; border-radius: 50%;
    background: linear-gradient(145deg, #e2e2e2, #7d7d7d);
  }
  .front-name {
    font-size: 38px; letter-spacing: 1px; color: var(--silver);
    text-transform: uppercase;
  }

  /* Back */
  .back-brand {
    position: absolute; left: 42px; top: 96px; width: 270px;
    display: flex; flex-direction: column; align-items: center; gap: 14px;
  }
  .back-brand .mark-dot { width: 56px; height: 56px; background: var(--white); }
  .back-name {
    font-size: 23px; color: var(--white); text-transform: uppercase;
    text-align: center; letter-spacing: 0.5px; white-space: nowrap;
  }
  .contact {
    position: absolute; left: 360px; top: 104px; color: var(--white);
    font-family: "Open Sans", sans-serif;
  }
  .person-name {
    font-family: "Montserrat", sans-serif; font-weight: 700; font-size: 27px;
  }
  .person-role { font-size: 13px; color: var(--muted); margin-top: 2px; }
  .contact-list { list-style: none; margin-top: 18px; font-size: 15px; }
  .contact-list li { display: flex; align-items: center; gap: 9px; margin-bottom: 4px; }
  .contact-list svg { width: 13px; height: 13px; flex: none; }
  .trust-badges { display: flex; align-items: center; gap: 10px; margin-top: 8px; }
  .badge-tile { width: 40px; height: 36px; border-radius: 4px; background: var(--badge-green); }
  .badge-ribbon { width: 70px; height: 18px; background: var(--badge-gold); }
  .bottom-band { position: absolute; left: 0; bottom: 0; width: 640px; height: 110px; }
  .site {
    position: absolute; right: 56px; bottom: 24px;
    font-family: "Open Sans", sans-serif; font-size: 16px; color: var(--white);
  }
</style>
</head>
<body>
  <section class="card card-front">
    <div class="front-mark">
      <div class="mark-dot"></div>
      <div class="front-name">Bright Lantern Studios</div>
    </div>
  </section>

  <section class="card card-back">
    <div class="back-brand">
      <div class="mark-dot"></div>
      <div class="back-name">Bright Lantern Studios</div>
    </div>

    <div class="contact">
      <div class="person-name">Doug Farley</div>
      <div class="person-role">Managing Partner</div>
      <ul class="contact-list">
        <li>
          <svg viewBox="0 0 16 16" aria-hidden="true"><circle cx="8" cy="8" r="7" fill="none" stroke="#fff" stroke-width="1.4"/><path d="M5.5 4.5l1.5 1.5-1 1c.5 1.2 1.5 2.2 2.7 2.7l1-1 1.5 1.5-1 1.2c-2.6-.4-4.7-2.5-5.1-5.1z" fill="#fff"/></svg>
          502-417-2356
        </li>
        <li>
          <svg viewBox="0 0 16 16" aria-hidden="true"><rect x="1" y="3" width="14" height="10" fill="none" stroke="#fff" stroke-width="1.4"/><path d="M1 3l7 6 7-6" fill="none" stroke="#fff" stroke-width="1.4"/></svg>
          Doug@BrightLanternStudios.com
        </li>
      </ul>
      <div class="trust-badges">
        <div class="badge-tile"></div>
        <div class="badge-ribbon"></div>
      </div>
    </div>

    <svg class="bottom-band" viewBox="0 0 640 110" aria-hidden="true">
      <path d="M0 62 L300 62 L300 72 L0 72 Z" fill="var(--band-light)"/>
      <path d="M318 110 L318 74 Q318 50 342 50 L640 50 L640 110 Z" fill="var(--band-dark)"/>
    </svg>
    <div class="site">www.BrightLanternStudios.com</div>
  </section>
</body>
</html>
```